New Brand - Website Design (4 Pages)

We are launching a new brand for electronic cigarettes. We already have logo and packaging done and would like a web design to go with it.

We are interested in the following deliverables:

1) Home Page Design
2) Check Out Design
3) How it Works Page
4) Secondary Template Page Design

Looking for a 60s modern look and something that is consistent with our logo and packaging.

Industry/Entity Type

Electronic

Requirements
Must have
• Consistent with logo and packaging (Use Logo Attached)
White background

Example (Functionality & Design): http://www.torvex.co.uk/
Example (Design): http://www.quillharbor.com/

We want the design more like quillharbor but the functionality the same as torvex.

Top Bar: Pebble Arcs Kits; Cartridge Refills; How it Works; Contact; My Account; Checkout
Should not have
• Stock List or Search Bar or Newsletter Signup

```html
<!DOCTYPE html>
<html lang="en">
<head>
<meta charset="utf-8">
<title>Pebble Arcs – Website Design</title>
<link rel="stylesheet" href="https://fonts.googleapis.com/css2?family=Open+Sans:wght@300;400;600;700&family=Great+Vibes&display=swap">
<style>
:root{
  --ink:#111;
  --bar:#0d0d0d;
  --blue:#1b8fd2;
  --blue-dark:#0f6fa8;
  --yellow:#f8ec8f;
  --yellow-edge:#c9b23c;
  --paper:#ffffff;
  --panel:#f1f1f1;
  --rule:#d6d6d6;
  --text:#3a3a3a;
  --muted:#8a8a8a;
  --sans:"Open Sans", Arial, sans-serif;
  --script:"Great Vibes", cursive;
}
*{box-sizing:border-box;margin:0;padding:0}
html,body{width:1200px;height:900px;overflow:hidden;background:var(--paper);font-family:var(--sans);color:var(--text)}
.stage{position:relative;width:1200px;height:900px}

/* page frames */
.page{position:absolute;background:var(--paper);box-shadow:0 2px 10px rgba(0,0,0,.18);overflow:hidden;display:flex;flex-direction:column}
.page--home{left:30px;top:205px;width:560px;height:490px}
.page--mini{top:300px;width:180px;height:300px;background:var(--panel)}
.page--checkout{left:620px}
.page--how{left:810px}
.page--product{left:1000px}

/* header */
.site-header{background:var(--bar);display:flex;align-items:center;border-bottom:2px solid var(--blue);flex:none}
.page--home .site-header{height:30px;padding:0 10px}
.page--mini .site-header{height:14px;padding:0 4px}
.brand{display:flex;align-items:center;gap:4px;color:#fff;font-weight:700;letter-spacing:.5px;white-space:nowrap}
.brand__dot{border-radius:50%;background:#fff;flex:none}
.page--home .brand{font-size:10px}
.page--home .brand__dot{width:14px;height:14px}
.page--mini .brand{font-size:4.5px;gap:2px}
.page--mini .brand__dot{width:7px;height:7px}
.main-nav{display:flex;margin-left:auto;color:#fff;font-weight:600;white-space:nowrap}
.page--home .main-nav{gap:14px;font-size:7.5px}
.page--mini .main-nav{gap:5px;font-size:3.2px}
.main-nav .is-active{color:var(--blue)}

/* hero */
.hero{position:relative;height:170px;flex:none;background:linear-gradient(90deg,#e9e4df 0%,#f4f2f0 45%,#fafafa 100%)}
.hero__photo{position:absolute;left:0;top:0;width:240px;height:100%;background:linear-gradient(90deg,#b89a86 0%,#d8c6b8 55%,rgba(240,236,232,0) 100%)}
.hero__copy{position:absolute;left:300px;top:30px;width:220px;text-align:center}
.hero__title{font-weight:300;font-size:21px;line-height:1.2;color:#3b3b3b}
.btn-order{display:inline-block;background:var(--yellow);border:1px solid var(--yellow-edge);color:#333;font-style:italic;font-weight:600;box-shadow:0 1px 2px rgba(0,0,0,.3)}
.hero .btn-order{margin-top:8px;font-size:10px;padding:3px 22px}

/* promise strip */
.promises{display:flex;align-items:center;height:58px;flex:none;border-bottom:1px solid var(--rule);background:#fff;padding:0 16px}
.promise{flex:1;display:flex;align-items:center;gap:10px;justify-content:center;color:var(--blue)}
.promise + .promise{border-left:1px solid var(--rule)}
.promise__title{font-size:7.5px;font-weight:700}
.promise__sub{font-size:5px;font-weight:600;color:var(--blue-dark)}
.coin{width:24px;height:24px;border-radius:50%;background:var(--blue);color:#fff;font-weight:700;font-size:13px;display:flex;align-items:center;justify-content:center}

/* products */
.products{flex:1;display:flex;gap:24px;padding:18px 30px;background:#fff}
.product{flex:1;display:flex;gap:10px}
.product__pack{width:70px;height:90px;flex:none;background:linear-gradient(160deg,#2a2a2a,#050505)}
.product__name{font-size:10px;font-weight:700;color:#222}
.product__text{font-size:6px;line-height:1.5;color:var(--muted);margin-top:4px}

/* footer band */
.promo-band{position:relative;background:linear-gradient(90deg,#1c1c1c,#3a3530 50%,#1c1c1c);display:flex;align-items:center;flex:none}
.page--home .promo-band{height:56px;padding:0 20px}
.page--mini .promo-band{height:30px;padding:0 6px;margin-top:auto}
.promo-band__photo{position:absolute;left:40%;top:0;width:25%;height:100%;background:linear-gradient(90deg,rgba(120,105,90,0),rgba(150,130,110,.6),rgba(120,105,90,0))}
.promo-band__script{position:relative;font-family:var(--script);color:#fff}
.page--home .promo-band__script{font-size:24px}
.page--mini .promo-band__script{font-size:11px}
.promo-band__sub{position:relative;color:#ccc;margin-left:8px}
.page--home .promo-band__sub{font-size:5.5px}
.page--mini .promo-band__sub{font-size:2.6px;margin-left:3px}
.promo-band .btn-order{position:relative;margin-left:auto}
.page--home .promo-band .btn-order{font-size:9px;padding:3px 18px}
.page--mini .promo-band .btn-order{font-size:4px;padding:1px 7px}
.site-footer{background:var(--bar);border-top:2px solid var(--blue);color:#888;flex:none}
.page--home .site-footer{height:14px;font-size:5px;padding:3px 10px}
.page--mini .site-footer{height:8px;font-size:2.6px;padding:2px 4px}

/* mini page body */
.mini-body{padding:5px 6px;flex:1;overflow:hidden}
.mini-title{font-weight:300;font-size:10px;color:#444;margin-bottom:4px}
.tiny{font-size:3px;line-height:1.45;color:var(--muted)}
.tiny strong{color:#333;font-size:3.4px}

/* checkout */
.checkout-step{display:inline-block;background:var(--blue);color:#fff;font-size:3.4px;font-weight:600;padding:1px 8px 1px 3px;clip-path:polygon(0 0,100% 0,92% 50%,100% 100%,0 100%);margin:3px 0}
.account{display:flex;gap:6px;margin:2px 0 4px}
.account__col{flex:1}
.account__col + .account__col{border-left:1px dotted var(--rule);padding-left:5px}
.radio{display:flex;align-items:center;gap:2px;margin-top:3px}
.radio::before{content:"";width:3px;height:3px;border:.5px solid #999;border-radius:50%}
.field{display:flex;align-items:center;gap:3px;margin-top:3px}
.field__input{flex:1;height:5px;background:#ddd}
.btn-blue{display:inline-block;background:var(--blue);color:#fff;font-size:3.2px;padding:1.5px 7px;margin-top:6px}
.steps-list{margin-top:14px;display:flex;flex-direction:column}

/* how it works */
.how-grid{display:grid;grid-template-columns:repeat(3,1fr);gap:6px 4px;padding-bottom:8px;border-bottom:1px solid var(--rule)}
.how-step{display:flex;gap:2px}
.how-step__num{width:9px;height:9px;border-radius:50%;background:var(--blue);color:#fff;font-size:5px;font-weight:700;display:flex;align-items:center;justify-content:center;flex:none}
.how-video{display:flex;align-items:center;gap:6px;margin-top:8px}
.how-video__screen{width:62px;height:42px;background:linear-gradient(135deg,#5a4a40,#1d1a18);border:2px solid #222;position:relative}
.how-video__screen::after{content:"";position:absolute;left:26px;top:15px;border-left:8px solid rgba(255,255,255,.85);border-top:5px solid transparent;border-bottom:5px solid transparent}
.how-video__label{font-weight:300;font-size:9px;line-height:1.2;color:#555;text-align:center}

/* product */
.product-detail{display:flex;gap:6px}
.gallery__main{width:70px;height:48px;background:linear-gradient(135deg,#f6f6f6,#cfcfcf)}
.gallery__thumbs{display:flex;gap:2px;margin-top:3px}
.gallery__thumbs span{width:8px;height:7px;background:#ccc}
.detail__name{font-weight:300;font-size:9px;color:#333}
.detail__price{font-size:4px;color:#555;margin:2px 0 3px;border-bottom:.5px solid var(--rule);padding-bottom:2px}
.accordion{margin-top:6px;margin-left:76px}
.accordion__head{font-size:3.4px;color:#444;border-bottom:.5px solid var(--rule);padding:2px 0}
</style>
</head>
<body>
<main class="stage">

  <!-- Home page -->
  <section class="page page--home" aria-label="Home page">
    <header class="site-header">
      <div class="brand"><span class="brand__dot"></span>PEBBLE ARCS</div>
      <nav class="main-nav"><span>Pebble Arcs Kits</span><span>Cartridge Refills</span><span>How it Works</span><span>Contact</span><span>My Account</span><span>Checkout</span><span>My Cart (0)</span></nav>
    </header>
    <div class="hero">
      <div class="hero__photo" role="img" aria-label="Photo of a woman holding an electronic cigarette"></div>
      <div class="hero__copy">
        <h1 class="hero__title">Everything you need<br>and more</h1>
        <span class="btn-order">Order Now</span>
      </div>
    </div>
    <div class="promises">
      <div class="promise">
        <div><p class="promise__title">30 DAY MONEY BACK PROMISE*</p><p class="promise__sub">NO QUIBBLES, HASSLE FREE RETURNS</p></div>
        <span class="coin">$</span>
      </div>
      <div class="promise">
        <div><p class="promise__title">FREE SHIPPING</p><p class="promise__sub">ON ORDERS $40 OR OVER</p></div>
        <svg width="32" height="20" viewBox="0 0 32 20" aria-hidden="true"><rect x="0" y="2" width="20" height="12" fill="#1b8fd2"/><path d="M21 6h6l4 5v3h-10z" fill="#1b8fd2"/><circle cx="6" cy="16" r="3" fill="#0f6fa8"/><circle cx="25" cy="16" r="3" fill="#0f6fa8"/></svg>
      </div>
      <div class="promise">
        <div><p class="promise__title">1 YEAR WARRANTY</p><p class="promise__sub">FOR ALL STARTER KITS</p></div>
        <span class="coin">1</span>
      </div>
    </div>
    <div class="products">
      <article class="product">
        <div class="product__pack" role="img" aria-label="Product box of a starter kit"></div>
        <div><h2 class="product__name">Lorem Ipsum</h2><p class="product__text">Lorem ipsum dolor sit amet, consectetur adipiscing elit. Aenean commodo ligula eget dolor.</p></div>
      </article>
      <article class="product">
        <div class="product__pack" role="img" aria-label="Product box of cartridge refills"></div>
        <div><h2 class="product__name">Lorem Ipsum</h2><p class="product__text">Lorem ipsum dolor sit amet, consectetur adipiscing elit. Aenean commodo ligula eget dolor.</p></div>
      </article>
    </div>
    <div class="promo-band">
      <div class="promo-band__photo" role="img" aria-label="Photo of a smoker in a dark setting"></div>
      <span class="promo-band__script">Lorem ipsum</span>
      <span class="promo-band__sub">Aenean massa. Cum sociis natoque penatibus et magnis.</span>
      <span class="btn-order">Order Now</span>
    </div>
    <footer class="site-footer">Copyright © 2013 Pebble Arcs. All rights reserved.</footer>
  </section>

  <!-- Checkout page -->
  <section class="page page--mini page--checkout" aria-label="Checkout page">
    <header class="site-header">
      <div class="brand"><span class="brand__dot"></span>PEBBLE ARCS</div>
      <nav class="main-nav"><span>Pebble Arcs Kits</span><span>Cartridge Refills</span><span>How it Works</span><span>Contact</span><span class="is-active">Checkout</span></nav>
    </header>
    <div class="mini-body">
      <h1 class="mini-title">Secure Checkout</h1>
      <span class="checkout-step">Step 1: Account Details</span>
      <div class="account tiny">
        <div class="account__col">
          <strong>I'm A New Customer</strong>
          <p>Register with us for faster checkout, to track the status of your order and more.</p>
          <p class="radio">Checkout as guest</p>
          <p class="radio">Register account</p>
          <span class="btn-blue">Continue</span>
        </div>
        <div class="account__col">
          <strong>I'm a returning customer</strong>
          <p>Enter your email and password below.</p>
          <p class="field">Email Address <span class="field__input"></span></p>
          <p class="field">Password <span class="field__input"></span></p>
          <p style="text-align:right;margin-top:1px">Forgot password?</p>
          <span class="btn-blue">Continue</span>
        </div>
      </div>
      <div class="steps-list">
        <span class="checkout-step">Step 2: Billing &amp; Account Details</span>
        <span class="checkout-step">Step 3: Shipping Details</span>
        <span class="checkout-step">Step 4: Shipping Method</span>
        <span class="checkout-step">Step 5: Order Confirmation</span>
      </div>
    </div>
    <div class="promo-band">
      <div class="promo-band__photo" role="img" aria-label="Photo of a smoker in a dark setting"></div>
      <span class="promo-band__script">Lorem ipsum</span>
      <span class="promo-band__sub">Aenean massa. Cum sociis natoque penatibus et magnis.</span>
      <span class="btn-order">Order Now</span>
    </div>
    <footer class="site-footer">Copyright © 2013 Pebble Arcs. All rights reserved.</footer>
  </section>

  <!-- How it works page -->
  <section class="page page--mini page--how" aria-label="How it works page">
    <header class="site-header">
      <div class="brand"><span class="brand__dot"></span>PEBBLE ARCS</div>
      <nav class="main-nav"><span>Pebble Arcs Kits</span><span>Cartridge Refills</span><span class="is-active">How it Works</span><span>Contact</span><span>Checkout</span></nav>
    </header>
    <div class="mini-body">
      <h1 class="mini-title">How it Works</h1>
      <div class="how-grid tiny">
        <div class="how-step"><span class="how-step__num">1</span><div><strong>Lorem Ipsum</strong><p>Lorem ipsum dolor sit amet, consectetur adipiscing elit. Aenean commodo ligula.</p></div></div>
        <div class="how-step"><span class="how-step__num">2</span><div><strong>Lorem Ipsum</strong><p>Lorem ipsum dolor sit amet, consectetur adipiscing elit. Aenean commodo ligula.</p></div></div>
        <div class="how-step"><span class="how-step__num">3</span><div><strong>Lorem Ipsum</strong><p>Lorem ipsum dolor sit amet, consectetur adipiscing elit. Aenean commodo ligula.</p></div></div>
        <div class="how-step"><span class="how-step__num">4</span><div><strong>Lorem Ipsum</strong><p>Lorem ipsum dolor sit amet, consectetur adipiscing elit. Aenean commodo ligula.</p></div></div>
        <div class="how-step"><span class="how-step__num">5</span><div><strong>Lorem Ipsum</strong><p>Lorem ipsum dolor sit amet, consectetur adipiscing elit. Aenean commodo ligula.</p></div></div>
        <div class="how-step"><span class="how-step__num">6</span><div><strong>Lorem Ipsum</strong><p>Lorem ipsum dolor sit amet, consectetur adipiscing elit. Aenean commodo ligula.</p></div></div>
      </div>
      <div class="how-video">
        <div class="how-video__screen" role="img" aria-label="Video still showing an electronic cigarette"></div>
        <svg width="22" height="10" viewBox="0 0 22 10" aria-hidden="true"><path d="M21 8C15 2 8 1 2 5" fill="none" stroke="#1b8fd2" stroke-width="1"/><path d="M2 5l4-3M2 5l4 2" stroke="#1b8fd2" stroke-width="1" fill="none"/></svg>
        <p class="how-video__label">Watch how<br>it works</p>
      </div>
    </div>
    <div class="promo-band">
      <div class="promo-band__photo" role="img" aria-label="Photo of a smoker in a dark setting"></div>
      <span class="promo-band__script">Lorem ipsum</span>
      <span class="promo-band__sub">Aenean massa. Cum sociis natoque penatibus et magnis.</span>
      <span class="btn-order">Order Now</span>
    </div>
    <footer class="site-footer">Copyright © 2013 Pebble Arcs. All rights reserved.</footer>
  </section>

  <!-- Product page -->
  <section class="page page--mini page--product" aria-label="Product page">
    <header class="site-header">
      <div class="brand"><span class="brand__dot"></span>PEBBLE ARCS</div>
      <nav class="main-nav"><span>Pebble Arcs Kits</span><span class="is-active">Cartridge Refills</span><span>How it Works</span><span>Contact</span><span>Checkout</span></nav>
    </header>
    <div class="mini-body">
      <div class="product-detail">
        <div>
          <div class="gallery__main" role="img" aria-label="Photo of a black electronic cigarette"></div>
          <div class="gallery__thumbs"><span></span><span></span><span></span><span></span></div>
        </div>
        <div class="tiny">
          <h1 class="detail__name">E-Cigarette</h1>
          <p class="detail__price">$ 00.000</p>
          <p>Flavour: Tobacco Original</p>
          <p>Quantity: 1</p>
          <span class="btn-blue">Add to Cart</span> <span>Add to wishlist</span>
        </div>
      </div>
      <div class="accordion tiny">
        <p class="accordion__head">Production Description</p>
        <p style="padding:2px 0">Lorem ipsum dolor sit amet, consectetur adipiscing elit. Aenean commodo ligula eget dolor massa.</p>
        <p class="accordion__head">Production Reviews</p>
      </div>
    </div>
    <div class="promo-band">
      <div class="promo-band__photo" role="img" aria-label="Photo of a smoker in a dark setting"></div>
      <span class="promo-band__script">Lorem ipsum</span>
      <span class="promo-band__sub">Aenean massa. Cum sociis natoque penatibus et magnis.</span>
      <span class="btn-order">Order Now</span>
    </div>
    <footer class="site-footer">Copyright © 2013 Pebble Arcs. All rights reserved.</footer>
  </section>

</main>
</body>
</html>
```